Business card design for a engineering company

I need a double sided business card design for my company "Verdmont Flow Solutions". The card will be used in Malaysia. Sleek and professional, with a little design flare to it.
Information to showcase:
1. Company logo
2. Name, title, phone, email address, website address
3. our products "Pumping technology, Valve & actuation, Air Moving Technology
Example:
Ravi Tanaka
Business manager
ravi.tanaka@verdmont-example.com
www.verdmont-example.com.my
- Pumping technology
- Valve & actuation
- Air moving technology
Target Market(s)
engineers, purchasing managers
Industry/Entity Type
Business
Contact Information for Business Card
Ravi Tanaka
Business manager
ravi.tanaka@verdmont-example.com
www.verdmont-example.com.my
- Pumping technology
- Valve & actuation
- Air moving technology
catch phrase : "Solving flow challenges, exceeding expectations"

```html
<!DOCTYPE html>
<html lang="en">
<head>
<meta charset="utf-8">
<title>Verdmont Flow Solutions – Business Card</title>
<link href="https://fonts.googleapis.com/css2?family=Lato:wght@400;700&family=Oswald:wght@300;400&display=swap" rel="stylesheet">
<style>
  :root {
    --bg: #162024;
    --card-dark: #0e2026;
    --card-mid: #3a3330;
    --card-orange: #ef7135;
    --ink-light: #ffffff;
    --ink-dark: #0d2a33;
    --accent: #f07c2c;
    --logo-panel: #e9e9e7;
  }
  * { box-sizing: border-box; margin: 0; padding: 0; }
  html, body {
    width: 1200px; height: 818px; overflow: hidden;
    background: var(--bg);
    font-family: "Lato", sans-serif;
  }
  .canvas {
    position: relative; width: 1200px; height: 818px;
  }
  .card {
    position: absolute; left: 290px; width: 620px; height: 371px;
    background: linear-gradient(180deg, var(--card-dark) 0%, var(--card-dark) 22%, var(--card-mid) 52%, var(--card-orange) 100%);
    color: var(--ink-light);
    overflow: hidden;
  }
  .card--front { top: 22px; }
  .card--back { top: 425px; }

  .logo-panel {
    position: absolute; left: 0; top: 58px; width: 266px; height: 57px;
    background: var(--logo-panel);
    display: flex; align-items: center; gap: 10px; padding-left: 40px;
  }
  .logo-dot { width: 24px; height: 24px; border-radius: 50%; background: var(--ink-dark); flex: none; }
  .logo-name {
    font-family: "Lato", sans-serif; font-weight: 700; color: var(--ink-dark);
    font-size: 15px; letter-spacing: 1px; line-height: 1.1; text-transform: uppercase;
  }

  .person { position: absolute; left: 300px; top: 64px; width: 200px; text-align: center; }
  .person__name {
    font-family: "Oswald", sans-serif; font-weight: 400; font-size: 27px;
    letter-spacing: 0.5px; line-height: 1;
  }
  .person__title {
    font-family: "Oswald", sans-serif; font-weight: 300; font-size: 15px;
    margin-top: 6px; text-transform: uppercase;
  }

  .contacts { position: absolute; left: 346px; top: 151px; list-style: none; }
  .contacts li {
    display: flex; align-items: center; gap: 12px; height: 27.5px;
    font-size: 15.5px;
  }
  .icon {
    width: 19px; height: 19px; border-radius: 4px; background: var(--accent);
    display: flex; align-items: center; justify-content: center; flex: none;
  }
  .icon svg { width: 13px; height: 13px; }

  .products { position: absolute; left: 43px; top: 206px; font-size: 13.5px; line-height: 22px; }
  .products ul { list-style: none; }
  .products li::before { content: "- "; }
  .tagline { padding-left: 5px; }

  .address {
    position: absolute; left: 282px; top: 308px;
    display: flex; align-items: center; gap: 9px; font-size: 15.5px;
  }
  .icon--pin { width: 19px; height: 19px; }

  .back-logo {
    position: absolute; left: 0; right: 0; top: 160px;
    display: flex; align-items: center; justify-content: center; gap: 18px;
  }
  .back-logo__dot { width: 64px; height: 64px; border-radius: 50%; background: var(--ink-dark); }
  .back-logo__name {
    font-family: "Lato", sans-serif; font-weight: 700; color: var(--ink-dark);
    font-size: 30px; letter-spacing: 3px; line-height: 1.15; text-transform: uppercase;
  }
</style>
</head>
<body>
<main class="canvas">

  <section class="card card--front" aria-label="Business card front">
    <div class="logo-panel">
      <span class="logo-dot"></span>
      <span class="logo-name">Verdmont<br>Flow Solutions</span>
    </div>

    <div class="person">
      <h1 class="person__name">RAVI TANAKA</h1>
      <p class="person__title">Business Manager</p>
    </div>

    <ul class="contacts">
      <li>
        <span class="icon"><svg viewBox="0 0 16 16"><path d="M4 1l3 3-2 2c1 2 3 4 5 5l2-2 3 3-2 3C7 15 1 9 1 3z" fill="#fff"/></svg></span>
        (03) 555 0142 88
      </li>
      <li>
        <span class="icon"><svg viewBox="0 0 16 16"><rect x="4" y="1" width="8" height="14" rx="1.5" fill="none" stroke="#fff" stroke-width="1.6"/><circle cx="8" cy="12.3" r="0.9" fill="#fff"/></svg></span>
        (012) 555 7316
      </li>
      <li>
        <span class="icon"><svg viewBox="0 0 16 16"><circle cx="8" cy="8" r="6.3" fill="none" stroke="#fff" stroke-width="1.5"/><ellipse cx="8" cy="8" rx="2.6" ry="6.3" fill="none" stroke="#fff" stroke-width="1.2"/><path d="M2 8h12" stroke="#fff" stroke-width="1.2"/></svg></span>
        www.verdmont-example.com.my
      </li>
      <li>
        <span class="icon"><svg viewBox="0 0 16 16"><rect x="1.5" y="3.5" width="13" height="9" rx="1" fill="none" stroke="#fff" stroke-width="1.5"/><path d="M2 4l6 5 6-5" fill="none" stroke="#fff" stroke-width="1.5"/></svg></span>
        ravi.tanaka@verdmont-example.com
      </li>
    </ul>

    <div class="products">
      <ul>
        <li>Pumping technology</li>
        <li>Valve &amp; actuation</li>
        <li>Air moving technology</li>
      </ul>
      <p class="tagline">Solving flow challenges, exceeding expectations</p>
    </div>

    <p class="address">
      <span class="icon icon--pin"><svg viewBox="0 0 16 16"><path d="M8 1a4.5 4.5 0 0 0-4.5 4.5C3.5 9 8 15 8 15s4.5-6 4.5-9.5A4.5 4.5 0 0 0 8 1z" fill="#fff"/><circle cx="8" cy="5.6" r="1.7" fill="#f07c2c"/></svg></span>
      418 Jalan Contoh, 50450, Malaysia
    </p>
  </section>

  <section class="card card--back" aria-label="Business card back">
    <div class="back-logo">
      <span class="back-logo__dot"></span>
      <span class="back-logo__name">Verdmont<br>Flow Solutions</span>
    </div>
  </section>

</main>
</body>
</html>
```